KORVAL RENOVATIONS AND CUSTOM BUILDS

5pages:
Home/ who we are , services offered, why us,
recent projects/ gallery , contact us

Industry/Entity Type

Design, renovations, project management

Coding

Coded - Design and coding required

Number of Pages Required

5+ page

Requirements
Should not have
• Too many colours

```html
<!DOCTYPE html>
<html lang="en">
<head>
<meta charset="utf-8">
<title>Korval Renovations</title>
<link href="https://fonts.googleapis.com/css2?family=Poppins:wght@400;500;600;700&display=swap" rel="stylesheet">
<style>
:root{
  --green:#79b82a;
  --green-dark:#5f9a18;
  --navy:#1d2646;
  --navy-2:#263158;
  --ink:#1f2433;
  --muted:#5d6170;
  --light:#eef0f3;
  --white:#ffffff;
}
*{box-sizing:border-box;margin:0;padding:0}
html,body{width:1200px;height:4464px;overflow:hidden}
body{position:relative;background:var(--white);font-family:"Poppins",sans-serif;color:var(--ink)}
section,header,footer{position:absolute;left:0;width:1200px}
.btn{display:inline-block;background:var(--green);color:var(--white);font-weight:600;font-size:15px;border-radius:20px;padding:8px 22px}

/* header */
.site-header{top:0;height:112px;background:var(--white);display:flex;align-items:center;padding:0 64px;justify-content:space-between;z-index:3}
.brand{display:flex;align-items:center;gap:10px}
.brand-dot{width:14px;height:14px;background:var(--green);border-radius:50%}
.brand-name{font-weight:700;font-size:20px;color:var(--navy);line-height:1.05}
.brand-name small{display:block;font-size:9px;letter-spacing:2px;font-weight:700;color:var(--navy)}
.main-nav{display:flex;align-items:center;gap:38px;font-size:15px;font-weight:500;color:var(--navy)}
.lang{display:flex;align-items:center;gap:6px}

/* hero */
.hero{top:112px;height:710px}
.hero-band{position:absolute;inset:0;background:var(--green);clip-path:polygon(0 0,100% 0,100% 100%,0 92%)}
.hero-photo{position:absolute;inset:0;background:linear-gradient(100deg,#6d5138 0%,#9a7a58 30%,#4b4b4b 60%,#3a3a3c 100%);clip-path:polygon(0 0,100% 0,100% 95%,0 88%)}
.hero-photo::after{content:"";position:absolute;inset:0;background:rgba(10,14,30,.35)}
.hero-title{position:absolute;top:268px;width:100%;text-align:center;color:var(--white);font-weight:700;font-size:48px;line-height:1.15;z-index:2}
.hero .btn{position:absolute;top:376px;left:50%;transform:translateX(-50%);z-index:2;font-size:14px}

.section-title{text-align:center;font-weight:700;font-size:30px;color:var(--navy)}
.section-title::after{content:"";display:block;width:60px;height:4px;background:var(--green);margin:8px auto 0}

/* what we do */
.what-we-do{top:860px;height:400px}
.what-we-do .lead{text-align:center;font-size:15px;color:var(--muted);margin-top:14px}
.sectors{display:flex;justify-content:center;gap:170px;margin-top:46px}
.sector{text-align:center;width:160px}
.sector svg{display:block;margin:0 auto}
.sector h3{font-size:18px;font-weight:600;margin-top:18px;color:var(--ink)}
.sector.active h3{color:var(--green)}

/* who we are */
.who-we-are{top:1270px;height:710px;background:var(--navy);clip-path:polygon(0 8%,100% 0,100% 92%,0 100%)}
.who-photo{position:absolute;left:152px;top:110px;width:448px;height:500px;border:8px solid var(--white);background:linear-gradient(160deg,#e6b43c 0%,#b9843e 45%,#6b5a48 100%)}
.who-text{position:absolute;left:640px;top:160px;width:420px;color:var(--white)}
.who-text h2{font-size:30px;font-weight:700}
.who-text h2::after{content:"";display:block;width:60px;height:4px;background:var(--green);margin-top:6px}
.who-text .intro{font-size:19px;line-height:1.45;margin-top:22px;font-weight:500}
.who-text p{font-size:13px;line-height:1.6;margin-top:14px;color:#c9cde0}
.who-text .btn{margin-top:30px}

/* services */
.services{top:2020px;height:580px}
.service-cards{display:flex;justify-content:center;gap:24px;margin-top:30px}
.card{width:228px;height:384px;background:var(--white);box-shadow:0 4px 18px rgba(0,0,0,.15);text-align:center}
.card-photo{height:170px}
.card h3{font-size:18px;font-weight:600;margin-top:20px;line-height:1.2}
.card p{font-size:12px;color:var(--muted);line-height:1.5;margin:10px 20px 0}
.card a{display:inline-block;margin-top:10px;font-size:13px;font-weight:600;color:var(--navy);border-bottom:2px solid var(--green)}
.card.featured{background:var(--green);color:var(--white)}
.card.featured p,.card.featured a{color:var(--white)}
.card.featured .card-photo{background:none;display:flex;align-items:flex-end;justify-content:center}
.services .see-more{position:absolute;left:50%;transform:translateX(-50%);top:500px;font-size:13px}

/* meaning */
.meaning{top:2632px;height:250px;background:var(--green);color:var(--white);text-align:center;padding-top:42px}
.meaning h2{font-size:30px;font-weight:700}
.meaning p{font-size:14px;line-height:1.7;margin:14px auto 0;width:860px;font-weight:500}

/* why us */
.why-us{top:2960px;height:500px}
.why-us h2{position:absolute;left:104px;top:0;font-size:30px;font-weight:700;color:var(--navy)}
.why-us h2::after{content:"";display:block;width:60px;height:4px;background:var(--green);margin-top:6px}
.reasons{position:absolute;left:104px;top:90px;list-style:none}
.reasons li{display:flex;align-items:center;gap:18px;font-size:19px;font-weight:500;height:60px}
.reason-icon{width:40px;height:40px;border-radius:50%;background:var(--navy);display:flex;align-items:center;justify-content:center}
.why-photo{position:absolute;left:628px;top:20px;width:420px;height:440px;background:linear-gradient(135deg,#e5e5e5 0%,#bdbdbd 50%,#5a5a5a 100%);border-right:10px solid var(--green);border-bottom:10px solid var(--green)}

/* area */
.area{top:3510px;height:620px;background:var(--light)}
.map-area{position:absolute;left:120px;top:100px;width:470px;height:390px;background:radial-gradient(ellipse at 50% 50%,#8a8d92 0%,#d4d6da 75%,var(--light) 100%)}
.area-list{position:absolute;left:660px;top:110px}
.area-list h2{font-size:30px;font-weight:700;color:var(--navy)}
.area-list h2::after{content:"";display:block;width:60px;height:4px;background:var(--green);margin-top:6px}
.area-list ul{list-style:none;margin-top:18px}
.area-list li{display:flex;align-items:center;gap:10px;font-size:22px;font-weight:500;height:44px}

/* footer */
.site-footer{top:4110px;height:354px;background:var(--navy);color:var(--white);clip-path:polygon(0 8%,100% 0,100% 100%,0 100%)}
.footer-accent{position:absolute;left:0;top:4096px;width:1200px;height:40px;background:var(--green);clip-path:polygon(0 70%,100% 0,100% 35%,0 100%)}
.footer-cols{position:absolute;top:60px;left:104px;display:flex;gap:0}
.footer-col h4{font-size:18px;font-weight:600;margin-bottom:12px}
.footer-col ul{list-style:none;font-size:13px;line-height:1.75;color:#d3d7e6}
.contact-item{display:flex;align-items:center;gap:10px;font-size:12px;color:#d3d7e6;margin-bottom:14px}
.ci-icon{width:30px;height:30px;border-radius:50%;background:var(--green);display:flex;align-items:center;justify-content:center;flex-shrink:0}
.form-row{display:flex;gap:8px}
.field{background:var(--white);color:#777;font-size:10px;padding:6px 8px;height:26px;margin-bottom:8px}
.field.msg{height:70px}
.form .btn{float:right;font-size:12px;padding:6px 16px}
.copyright{position:absolute;bottom:18px;width:100%;text-align:center;font-size:11px;color:#c2c6d6}
</style>
</head>
<body>

<header class="site-header">
  <div class="brand">
    <span class="brand-dot"></span>
    <div class="brand-name">KORVAL<br>RENOVATIONS<small>AND CUSTOM BUILDS</small></div>
  </div>
  <nav class="main-nav">
    <span>Home</span><span>Who We Are</span><span>What We Do</span><span>Our Services</span><span>Contact Us</span>
    <span class="lang"><svg width="14" height="14" viewBox="0 0 14 14"><circle cx="7" cy="7" r="6" fill="none" stroke="#1d2646" stroke-width="1.4"/><path d="M1 7h12M7 1c3 3 3 9 0 12M7 1c-3 3-3 9 0 12" fill="none" stroke="#1d2646" stroke-width="1"/></svg>Eng</span>
    <span class="btn">Log In</span>
  </nav>
</header>

<section class="hero">
  <div class="hero-band"></div>
  <div class="hero-photo" role="img" aria-label="Interior under renovation with open wood framing and grey double doors"></div>
  <h1 class="hero-title">WELCOME TO<br>KORVAL RENOVATIONS</h1>
  <span class="btn">Get Started</span>
</section>

<section class="what-we-do">
  <h2 class="section-title">WHAT WE DO</h2>
  <p class="lead">We design, execute, and manage any construction project whether it's residential/commercial, or institutional</p>
  <div class="sectors">
    <div class="sector">
      <svg width="150" height="150" viewBox="0 0 150 150"><polygon points="75,4 137,40 137,110 75,146 13,110 13,40" fill="#1d2646"/><rect x="55" y="45" width="40" height="60" fill="#fff"/><g fill="#1d2646"><rect x="62" y="53" width="8" height="8"/><rect x="80" y="53" width="8" height="8"/><rect x="62" y="68" width="8" height="8"/><rect x="80" y="68" width="8" height="8"/><rect x="70" y="88" width="10" height="17"/></g></svg>
      <h3>Residential</h3>
    </div>
    <div class="sector active">
      <svg width="150" height="150" viewBox="0 0 150 150"><polygon points="75,4 137,40 137,110 75,146 13,110 13,40" fill="#79b82a"/><polygon points="75,12 130,44 130,106 75,138 20,106 20,44" fill="none" stroke="#fff" stroke-width="2"/><rect x="48" y="50" width="54" height="55" fill="#fff"/><g fill="#79b82a"><rect x="55" y="58" width="9" height="9"/><rect x="70" y="58" width="9" height="9"/><rect x="85" y="58" width="9" height="9"/><rect x="55" y="73" width="9" height="9"/><rect x="70" y="73" width="9" height="9"/><rect x="85" y="73" width="9" height="9"/><rect x="69" y="90" width="12" height="15"/></g></svg>
      <h3>Commercial</h3>
    </div>
    <div class="sector">
      <svg width="150" height="150" viewBox="0 0 150 150"><polygon points="75,4 137,40 137,110 75,146 13,110 13,40" fill="#1d2646"/><polygon points="75,42 108,60 42,60" fill="#fff"/><rect x="46" y="64" width="58" height="36" fill="#fff"/><g fill="#1d2646"><rect x="52" y="70" width="6" height="24"/><rect x="64" y="70" width="6" height="24"/><rect x="80" y="70" width="6" height="24"/><rect x="92" y="70" width="6" height="24"/></g><rect x="40" y="102" width="70" height="6" fill="#fff"/></svg>
      <h3>Institutional</h3>
    </div>
  </div>
</section>

<section class="who-we-are">
  <div class="who-photo" role="img" aria-label="Team of construction workers in hard hats and tool belts"></div>
  <div class="who-text">
    <h2>WHO WE ARE</h2>
    <p class="intro">A Team of professionals with over 25 years of combined experience in all sectors of the building field with design, trades, and construction management</p>
    <p>We plan every project with care, from first sketch to final walkthrough. Our crews keep sites clean, schedules honest and budgets clear, so each client knows what happens next and why it matters for their space.</p>
    <span class="btn">Read More</span>
  </div>
</section>

<section class="services">
  <h2 class="section-title">SERVICES OFFERED</h2>
  <div class="service-cards">
    <div class="card">
      <div class="card-photo" role="img" aria-label="Basement with exposed wooden joists" style="background:linear-gradient(160deg,#8a5a32,#4a2f1c)"></div>
      <h3>Finishing<br>Basements</h3>
      <p>We turn bare basements into warm, dry living space built to last for years.</p>
      <a>Read More</a>
    </div>
    <div class="card">
      <div class="card-photo" role="img" aria-label="Commercial interior being renovated" style="background:linear-gradient(160deg,#b5aa9a,#5b4e42)"></div>
      <h3>commercial<br>Renovations</h3>
      <p>Offices and retail units refitted on schedule with little disruption to business.</p>
      <a>Read More</a>
    </div>
    <div class="card featured">
      <div class="card-photo"><svg width="90" height="110" viewBox="0 0 90 110"><rect x="14" y="30" width="50" height="8" rx="3" fill="#1d2646"/><path d="M20 40h38v20a19 19 0 0 1-38 0z" fill="#1d2646"/><rect x="40" y="8" width="6" height="24" fill="#1d2646"/><path d="M46 8h16v6H46z" fill="#1d2646"/><rect x="26" y="84" width="32" height="16" rx="3" fill="#fff"/></svg></div>
      <h3>Bathroom<br>Renovations</h3>
      <p>Fresh tile, fixtures and storage for a bathroom that works for your home.</p>
      <a>Read More</a>
    </div>
    <div class="card">
      <div class="card-photo" role="img" aria-label="Newly built custom home interior" style="background:linear-gradient(160deg,#6a4d3a,#2f2622)"></div>
      <h3>Custom<br>Homes</h3>
      <p>Homes designed and built around the way you live, from plan to keys.</p>
      <a>Read More</a>
    </div>
  </div>
  <span class="btn see-more">See More</span>
</section>

<section class="meaning">
  <h2>WHAT THIS REALLY MEANS</h2>
  <p>Our Team Does: Demolition, Cutting Doors | Windows, Framing, Thermal Insulation, Soundproofing, Drywalling, Painting, Flooring, Doors, Trims, Kitchen Cabinets<br>Our Subcontractors Do: Plumbing, Electrical, Taping, and Tiling</p>
</section>

<section class="why-us">
  <h2>WHY US</h2>
  <ul class="reasons">
    <li><span class="reason-icon"><svg width="18" height="18" viewBox="0 0 18 18"><path d="M3 9l4 4 8-8" fill="none" stroke="#fff" stroke-width="2.4"/></svg></span>Competitive Rates</li>
    <li><span class="reason-icon"><svg width="18" height="18" viewBox="0 0 18 18"><path d="M3 9l4 4 8-8" fill="none" stroke="#fff" stroke-width="2.4"/></svg></span>Licensed Subcontractors</li>
    <li><span class="reason-icon"><svg width="18" height="18" viewBox="0 0 18 18"><path d="M3 9l4 4 8-8" fill="none" stroke="#fff" stroke-width="2.4"/></svg></span>Wide Network Of Consultants</li>
    <li><span class="reason-icon"><svg width="18" height="18" viewBox="0 0 18 18"><path d="M3 9l4 4 8-8" fill="none" stroke="#fff" stroke-width="2.4"/></svg></span>Suppliers List Suits Every Budget</li>
    <li><span class="reason-icon"><svg width="18" height="18" viewBox="0 0 18 18"><path d="M3 9l4 4 8-8" fill="none" stroke="#fff" stroke-width="2.4"/></svg></span>Flexible Working Hours</li>
  </ul>
  <div class="why-photo" role="img" aria-label="Close-up of renovation work on an interior wall with tools"></div>
</section>

<section class="area">
  <div class="map-area" role="img" aria-label="Map of Canada with the Ontario service area marked"></div>
  <div class="area-list">
    <h2>AREA WE COVER</h2>
    <ul>
      <li><svg width="14" height="18" viewBox="0 0 14 18"><path d="M7 0a7 7 0 0 1 7 7c0 5-7 11-7 11S0 12 0 7a7 7 0 0 1 7-7z" fill="#79b82a"/><circle cx="7" cy="7" r="2.5" fill="#eef0f3"/></svg>Scarborough,On</li>
      <li><svg width="14" height="18" viewBox="0 0 14 18"><path d="M7 0a7 7 0 0 1 7 7c0 5-7 11-7 11S0 12 0 7a7 7 0 0 1 7-7z" fill="#79b82a"/><circle cx="7" cy="7" r="2.5" fill="#eef0f3"/></svg>Oakville</li>
      <li><svg width="14" height="18" viewBox="0 0 14 18"><path d="M7 0a7 7 0 0 1 7 7c0 5-7 11-7 11S0 12 0 7a7 7 0 0 1 7-7z" fill="#79b82a"/><circle cx="7" cy="7" r="2.5" fill="#eef0f3"/></svg>Bowmanville</li>
      <li><svg width="14" height="18" viewBox="0 0 14 18"><path d="M7 0a7 7 0 0 1 7 7c0 5-7 11-7 11S0 12 0 7a7 7 0 0 1 7-7z" fill="#79b82a"/><circle cx="7" cy="7" r="2.5" fill="#eef0f3"/></svg>Barrie</li>
    </ul>
  </div>
</section>

<div class="footer-accent"></div>
<footer class="site-footer">
  <div class="footer-cols">
    <div class="footer-col" style="width:184px">
      <h4>Quick Links</h4>
      <ul><li>Home</li><li>Who We Are</li><li>What We Do</li><li>Our Services</li><li>Contact Us</li></ul>
    </div>
    <div class="footer-col" style="width:208px">
      <h4>Help Links</h4>
      <ul><li>Terms &amp; conditions</li><li>Privacy Policy</li><li>Testimonials</li><li>Support</li></ul>
    </div>
    <div class="footer-col" style="width:324px">
      <h4>Contact</h4>
      <div class="contact-item"><span class="ci-icon"><svg width="12" height="14" viewBox="0 0 14 18"><path d="M7 0a7 7 0 0 1 7 7c0 5-7 11-7 11S0 12 0 7a7 7 0 0 1 7-7z" fill="#fff"/></svg></span>48 Brimley Crest,<br>Scarborough, On</div>
      <div class="contact-item"><span class="ci-icon"><svg width="14" height="14" viewBox="0 0 14 14"><path d="M3 1l3 3-2 2c1 2 2 3 4 4l2-2 3 3-2 2C6 13 1 8 1 3z" fill="#fff"/></svg></span>(416) 555-0187</div>
      <div class="contact-item"><span class="ci-icon"><svg width="14" height="12" viewBox="0 0 14 12"><rect x="1" y="1" width="12" height="10" fill="none" stroke="#fff" stroke-width="1.5"/><path d="M1 1l6 5 6-5" fill="none" stroke="#fff" stroke-width="1.5"/></svg></span>hello@korvalbuilds.com</div>
    </div>
    <div class="footer-col form" style="width:212px">
      <h4>Get In Touch</h4>
      <div class="form-row"><div class="field" style="flex:1">Name</div><div class="field" style="flex:1">Phone</div></div>
      <div class="field">Email</div>
      <div class="field msg">Message</div>
      <span class="btn">Submit</span>
    </div>
  </div>
  <p class="copyright">Copyright © 2020 Korval Renovations. All Rights Reserved. | Privacy policy</p>
</footer>

</body>
</html>
```